Business card for Cat Cafe

I have started a small business and need a business card designed. The business is a cat cafe, that is, an ordinary cafe that serves coffee and snacks but with a twist - you can bring your cat to play. In fact the idea is to encourage everyone to come and bring your feline friend in order to build community and provide some fun and connections between fellow cat lovers. Themes of the business include;

- Fun
- Discovery
- Connections

The name of the cafe is Brews and Whiskers!

We look forward to seeing what creative ideas you may have!
Updates

Hi,

 Please note the contact details as below;
14 Tarrant Lane, Marlow Vale,
Kellerton, VIC
3158

Target Market(s)

Cat owners, any age group

Industry/Entity Type

Small Business

Requirements
Must have
• Must include some type of imagery of a cat itself.

```html
<!DOCTYPE html>
<html lang="en">
<head>
<meta charset="utf-8">
<title>Brews and Whiskers! – Business Card</title>
<link rel="stylesheet" href="https://fonts.googleapis.com/css2?family=Roboto:wght@700;900&display=swap">
<style>
  :root {
    --page-bg: #dcdcdc;
    --card-white: #ffffff;
    --brand-red: #b81f26;
    --brand-red-deep: #9c1b20;
    --brand-orange: #e0662a;
    --brand-amber: #f2a51e;
    --phone-gold: #f6a623;
    --text-light: #ffffff;
    --name-red: #a81c22;
    --art-warm: #f4b43a;
    --art-soft: #f9d98a;
  }
  * { margin: 0; padding: 0; box-sizing: border-box; }
  html, body {
    width: 1200px;
    height: 900px;
    overflow: hidden;
    background: var(--page-bg);
    font-family: "Roboto", Arial, sans-serif;
  }
  .business-card {
    position: absolute;
    left: 160px;
    top: 200px;
    width: 880px;
    height: 500px;
    border-radius: 40px;
    overflow: hidden;
    background: var(--card-white);
  }
  .card-backdrop {
    position: absolute;
    inset: 0;
    width: 100%;
    height: 100%;
  }
  .mascot-art {
    position: absolute;
    left: 220px;
    top: 70px;
    width: 290px;
    height: 220px;
    border-radius: 24px;
    background: radial-gradient(circle at 40% 45%, var(--art-soft), var(--art-warm) 75%);
  }
  .brand-name {
    position: absolute;
    left: 40px;
    top: 318px;
    width: 440px;
    font-weight: 900;
    font-size: 46px;
    line-height: 1.1;
    color: var(--name-red);
  }
  .contact-block {
    position: absolute;
    left: 610px;
    top: 104px;
    width: 270px;
    text-align: center;
    font-weight: 700;
  }
  .contact-phone {
    font-size: 32px;
    color: var(--phone-gold);
    margin-bottom: 36px;
    letter-spacing: 0.5px;
  }
  .contact-address {
    font-style: normal;
    font-size: 24px;
    line-height: 37px;
    color: var(--text-light);
  }
</style>
</head>
<body>
  <div class="business-card">
    <svg class="card-backdrop" viewBox="0 0 880 500" preserveAspectRatio="none" aria-hidden="true">
      <defs>
        <linearGradient id="swoosh-gradient" x1="0" y1="0" x2="0" y2="1">
          <stop offset="0" stop-color="var(--brand-orange)"/>
          <stop offset="1" stop-color="var(--brand-amber)"/>
        </linearGradient>
        <linearGradient id="panel-gradient" x1="0" y1="0" x2="0" y2="1">
          <stop offset="0" stop-color="var(--brand-red)"/>
          <stop offset="1" stop-color="var(--brand-red-deep)"/>
        </linearGradient>
      </defs>
      <path class="accent-swoosh" d="M445 0 H552 C560 200 520 380 440 460 C510 340 505 170 445 0 Z" fill="url(#swoosh-gradient)"/>
      <path class="contact-panel" d="M565 0 H880 V500 H420 C525 380 575 200 565 0 Z" fill="url(#panel-gradient)"/>
    </svg>

    <div class="mascot-art" role="img" aria-label="Cartoon tabby cat mascot holding a tray with a drink, burger and fries"></div>
    <div class="brand-name">Brews and Whiskers!</div>

    <div class="contact-block">
      <p class="contact-phone">1800 555 247</p>
      <address class="contact-address">
        14 Tarrant Lane,<br>
        Marlow Vale,<br>
        Kellerton, VIC<br>
        3158
      </address>
    </div>
  </div>
</body>
</html>
```